Looking for updated Letterhead and Compliments Slips to go with our new updated logo. This stationary will be used for letters to suppliers and customers so needs to be practical while also quite classic.

We are an engineering company so needs to be clean and precise

Target Market(s)

SME'S and large automotive customers

Industry/Entity Type

Automotive

Font styles to use
Sans Serif

Colors
85acd3
0356a4
0792cd
33a6d7
85abd2
ffffff

Requirements
Must have
• Address details as below
• KT Fabrications Limited
• Hallmere Road
• Brackford
• Elmshire
• LP47 9XZ, UK
• Telephone: +44 (0)1632 960418
• Fax: +44 (0)1632 960733
• Email: sales@ktfabrications.example
• Web: www.ktfabrications.example
Nice to have
• Nice to have some element of being a British Manufacturer

```html
<!DOCTYPE html>
<html lang="en">
<head>
<meta charset="utf-8">
<title>KT Fabrications Limited – Letterhead</title>
<link rel="stylesheet" href="https://fonts.googleapis.com/css2?family=Montserrat:wght@400&family=Nunito+Sans:wght@400&family=Source+Sans+3:wght@400;700&display=swap">
<style>
  :root {
    --brand-blue: #0356a4;
    --brand-blue-deep: #155a9c;
    --text-dark: #444a50;
    --text-mid: #5a5f66;
    --watermark: #efefef;
    --footer-grey: #ececec;
    --white: #ffffff;
  }
  * { margin: 0; padding: 0; box-sizing: border-box; }
  html, body { width: 849px; height: 1200px; overflow: hidden; background: var(--white); }
  .letterhead {
    position: relative;
    width: 849px;
    height: 1200px;
    overflow: hidden;
    background: var(--white);
    font-family: "Nunito Sans", sans-serif;
  }

  .brand-name {
    position: absolute;
    left: 28px;
    top: 52px;
    display: flex;
    align-items: center;
    gap: 10px;
    color: var(--brand-blue);
    font-family: "Montserrat", sans-serif;
    font-size: 19px;
    line-height: 1.15;
    letter-spacing: 0.04em;
  }
  .brand-name .brand-square {
    width: 18px;
    height: 18px;
    background: var(--brand-blue);
    flex: none;
  }

  .address {
    position: absolute;
    left: 696px;
    top: 56px;
    display: flex;
    gap: 9px;
    font-style: normal;
  }
  .address .pin { width: 18px; height: 18px; flex: none; margin-top: 1px; }
  .address p {
    font-size: 15px;
    line-height: 19px;
    color: var(--text-dark);
    white-space: nowrap;
  }

  .watermark {
    position: absolute;
    left: 0;
    right: 0;
    top: 430px;
    text-align: center;
    font-family: "Montserrat", sans-serif;
    color: var(--watermark);
    line-height: 1.05;
  }
  .watermark .wm-line-1 { display: block; font-size: 150px; letter-spacing: 0.08em; }
  .watermark .wm-line-2 { display: block; font-size: 78px; letter-spacing: 0.06em; }

  .footer-fade {
    position: absolute;
    left: 0; right: 0; bottom: 0;
    height: 170px;
    background: linear-gradient(to bottom, var(--white), var(--footer-grey));
  }
  .footer-waves {
    position: absolute;
    left: 0; top: 1030px;
    width: 849px; height: 170px;
  }

  .footer-name {
    position: absolute;
    left: 51px;
    top: 1137px;
    color: var(--white);
    font-family: "Montserrat", sans-serif;
    font-size: 22px;
    letter-spacing: 0.4em;
    white-space: nowrap;
  }

  .contacts {
    position: absolute;
    top: 1111px;
    display: grid;
    row-gap: 4px;
  }
  .contacts.phones { left: 470px; }
  .contacts.online { left: 620px; }
  .contact-item {
    display: flex;
    align-items: center;
    gap: 7px;
    font-family: "Source Sans 3", sans-serif;
    font-size: 12px;
    line-height: 14px;
    color: var(--text-mid);
    white-space: nowrap;
  }
  .contact-item svg { width: 12px; height: 12px; flex: none; }
  .contact-item b { font-weight: 700; color: var(--text-dark); }
</style>
</head>
<body>
<main class="letterhead">

  <div class="brand-name">
    <span class="brand-square"></span>
    <span>KT<br>Fabrications</span>
  </div>

  <address class="address">
    <svg class="pin" viewBox="0 0 18 18" aria-hidden="true">
      <rect width="18" height="18" rx="4" fill="var(--brand-blue)"/>
      <path d="M9 3.5a3.6 3.6 0 0 0-3.6 3.6c0 2.7 3.6 6.6 3.6 6.6s3.6-3.9 3.6-6.6A3.6 3.6 0 0 0 9 3.5z" fill="none" stroke="#fff" stroke-width="1.3"/>
      <circle cx="9" cy="7.1" r="1.2" fill="#fff"/>
    </svg>
    <p>Hallmere Road<br>Brackford<br>Elmshire<br>LP47 9XZ, UK</p>
  </address>

  <div class="watermark" aria-hidden="true">
    <span class="wm-line-1">KT</span>
    <span class="wm-line-2">Fabrications</span>
  </div>

  <div class="footer-fade"></div>

  <svg class="footer-waves" viewBox="0 1030 849 170" aria-hidden="true">
    <path d="M0 1112 C70 1052 220 1042 340 1083 C385 1098 420 1114 452 1130" fill="none" stroke="var(--brand-blue-deep)" stroke-width="2.5"/>
    <path d="M0 1200 L0 1128 C60 1070 200 1058 310 1092 C400 1120 450 1165 520 1200 Z" fill="var(--brand-blue-deep)"/>
    <path d="M560 1190 C690 1185 800 1160 849 1112" fill="none" stroke="var(--brand-blue-deep)" stroke-width="2.5"/>
    <path d="M585 1200 C700 1196 790 1175 849 1125 L849 1200 Z" fill="var(--brand-blue-deep)"/>
  </svg>

  <div class="footer-name">KT FABRICATIONS</div>

  <div class="contacts phones">
    <div class="contact-item">
      <svg viewBox="0 0 12 12" aria-hidden="true"><rect width="12" height="12" rx="3" fill="var(--brand-blue)"/><path d="M4 2.8c.4 0 .9 1.4.6 1.8l-.5.5c.4 1 1.3 1.9 2.3 2.3l.5-.5c.4-.3 1.8.2 1.8.6 0 .7-.7 1.4-1.4 1.4C5 8.9 3.1 7 3.1 4.2c0-.7.4-1.4.9-1.4z" fill="#fff"/></svg>
      <span>+44 (0)1632 960418</span>
    </div>
    <div class="contact-item">
      <svg viewBox="0 0 12 12" aria-hidden="true"><rect width="12" height="12" rx="3" fill="var(--brand-blue)"/><rect x="4" y="2.5" width="4" height="2.5" fill="#fff"/><rect x="2.5" y="5" width="7" height="3" rx=".6" fill="#fff"/><rect x="4" y="7.5" width="4" height="2" fill="#fff" stroke="var(--brand-blue)" stroke-width=".5"/></svg>
      <span>+44 (0)1632 960733</span>
    </div>
  </div>

  <div class="contacts online">
    <div class="contact-item">
      <svg viewBox="0 0 12 12" aria-hidden="true"><rect width="12" height="12" rx="3" fill="var(--brand-blue)"/><rect x="2.5" y="3.5" width="7" height="5" fill="#fff"/><path d="M2.5 3.5 6 6.3 9.5 3.5" fill="none" stroke="var(--brand-blue)" stroke-width=".8"/></svg>
      <span>sales@<b>ktfabrications</b>.example</span>
    </div>
    <div class="contact-item">
      <svg viewBox="0 0 12 12" aria-hidden="true"><rect width="12" height="12" rx="3" fill="var(--brand-blue)"/><circle cx="6" cy="6" r="3.4" fill="none" stroke="#fff" stroke-width=".8"/><ellipse cx="6" cy="6" rx="1.4" ry="3.4" fill="none" stroke="#fff" stroke-width=".7"/><path d="M2.6 6h6.8" stroke="#fff" stroke-width=".7"/></svg>
      <span>www.<b>ktfabrications</b>.example</span>
    </div>
  </div>

</main>
</body>
</html>
```